Tembo & Lusani Advocates website

An interactive professional law firm website fully synchronized with social media pages.

Target Market(s)

Corporations and professionals

Industry/Entity Type

Professional Service

Number of Pages Required

5+ page

Font styles to use
Sans Serif

Colors

Designer to choose colors to be used in the design.

```html
<!DOCTYPE html>
<html lang="en">
<head>
<meta charset="utf-8">
<title>Tembo &amp; Lusani Advocates</title>
<link href="https://fonts.googleapis.com/css2?family=Roboto:wght@300;400;500;700&display=swap" rel="stylesheet">
<style>
:root{
  --red:#9b1a27;
  --red-dark:#7e121d;
  --ink:#1d1d1d;
  --muted:#555;
  --light:#f4f4f4;
  --white:#fff;
  --sans:"Roboto",Arial,sans-serif;
}
*{box-sizing:border-box;margin:0;padding:0}
html,body{width:1200px;height:3416px;overflow:hidden;background:var(--white);font-family:var(--sans);color:var(--ink)}
.page{position:relative;width:1200px;height:3416px}
.abs{position:absolute}
.center{text-align:center}

/* header */
.brand{left:118px;top:40px;display:flex;align-items:center;gap:12px}
.brand-square{width:22px;height:22px;background:var(--red)}
.brand-name{font-family:var(--sans);font-weight:500;font-size:26px;color:var(--red)}
.brand-tag{left:118px;top:96px;font-size:9px;letter-spacing:2px;color:var(--red)}
.head-contact{top:58px;display:flex;align-items:center;gap:12px;font-size:15px;color:#333}
.ico-ring{width:32px;height:32px;border:2px solid var(--red);border-radius:50%;display:flex;align-items:center;justify-content:center}

/* nav */
.nav{left:0;top:148px;width:1200px;height:39px;background:var(--red)}
.nav ul{list-style:none;display:flex;position:absolute;left:118px;top:0;height:39px}
.nav li{color:var(--white);font-size:14px;line-height:39px;padding:0 17px}
.nav li.active{background:var(--red-dark)}

/* hero */
.hero{left:0;top:187px;width:1200px;height:523px;background:linear-gradient(120deg,#6d6a66 0%,#a9a49d 40%,#d7d2cb 60%,#4b3a2c 100%)}
.hero-title{left:0;width:1200px;top:424px;font-weight:700;font-size:36px;color:var(--white)}
.btn{background:var(--red);color:var(--white);font-weight:500;font-size:15px;border-radius:4px;display:flex;align-items:center;justify-content:center}
.arrow{width:34px;height:34px;border-radius:50%;border:2px solid #222;background:rgba(255,255,255,.6);display:flex;align-items:center;justify-content:center}

/* headings */
.sec-title{left:0;width:1200px;font-size:36px;font-weight:500;color:#111}
.sec-sub{left:0;width:1200px;font-size:14px;color:#333}

/* services */
.svc-photo{width:250px;height:250px;border-radius:50%;border:8px solid #eee}
.svc-name{width:300px;font-size:18px;letter-spacing:.5px;color:#111}
.svc-text{width:280px;font-size:14px;line-height:16px;color:#333}

/* professionals */
.pro{left:0;top:1400px;width:1200px;height:540px;background:radial-gradient(ellipse at 55% 40%,#4a2e22 0%,#25160f 50%,#120b08 100%)}
.pro-title{left:0;width:1200px;top:1562px;font-size:38px;color:var(--white)}
.pro-sub{left:0;width:1200px;top:1618px;font-size:14px;color:var(--white)}
.stat{width:300px;color:var(--white);text-align:center}
.stat-label{font-weight:700;font-size:19px;margin-top:10px}
.stat-num{font-weight:700;font-size:19px;margin-top:8px}

/* team */
.member-photo{width:218px;height:218px;border-radius:50%;border:3px solid #222;background:linear-gradient(160deg,#2f5e86 0%,#1c3a56 55%,#0f2233 100%)}
.member-name{width:260px;font-weight:500;font-size:21px;color:#222}
.member-role{width:260px;font-weight:300;font-size:19px;color:#444;margin-top:4px}
.socials{display:flex;gap:6px;justify-content:center}
.socials span{width:26px;height:26px;border-radius:50%;background:#3a3a3a}
.dot{width:9px;height:9px;border-radius:50%;background:#222}

/* practice tabs */
.tab{width:320px;font-size:24px;line-height:30px;color:#222}
.tab.active{color:var(--red)}
.tab-line{left:501px;top:2596px;width:264px;height:3px;background:var(--red)}

/* clients */
.client{font-weight:700;font-size:20px;color:var(--red);display:flex;align-items:center;gap:8px;transform:translateX(-50%)}
.client i{display:block;width:14px;height:14px;background:var(--red);border-radius:50%}
.arrow-sm{width:26px;height:26px;border-radius:50%;background:#222;display:flex;align-items:center;justify-content:center}

/* newsletter */
.news{left:0;top:2798px;width:1200px;height:233px;background:var(--light)}
.news-title{left:0;width:1200px;top:2870px;font-size:28px;color:#222}
.news-sub{left:0;width:1200px;top:2906px;font-size:14px;color:#444}
.news-input{left:335px;top:2942px;width:378px;height:30px;background:#e8e8e8;border-radius:15px 0 0 15px;font-size:13px;color:#777;padding-left:20px;line-height:30px}
.news-btn{left:713px;top:2942px;width:130px;height:30px;background:var(--red);border-radius:0 15px 15px 0;color:var(--white);font-size:13px;line-height:30px;text-align:center}

/* footer */
.footer{left:0;top:3031px;width:1200px;height:325px;background:var(--red)}
.foot-logo{left:118px;top:3108px;width:264px;height:82px;background:var(--white);display:flex;flex-direction:column;align-items:flex-start;justify-content:center;padding-left:14px}
.foot-logo .row{display:flex;align-items:center;gap:8px}
.foot-logo .brand-square{width:14px;height:14px}
.foot-logo .brand-name{font-size:17px}
.foot-logo small{font-size:7px;letter-spacing:1.5px;color:var(--red);margin-top:8px}
.foot-text{color:var(--white);font-size:14px;line-height:19px}
.foot-head{color:var(--white);font-size:14px;font-weight:500}
.foot-rule{height:2px;width:64px;background:var(--white);margin-top:14px}
.field{background:#b8404c;height:24px;font-size:11px;color:var(--white);padding:5px 8px}
.copyright{left:118px;top:3372px;font-size:14px;color:#333}
.copy-social{right:118px;top:3368px;display:flex;gap:10px}
.copy-social span{width:24px;height:24px;border-radius:50%;background:var(--red)}
</style>
</head>
<body>
<div class="page">

  <!-- header -->
  <div class="abs brand">
    <span class="brand-square"></span>
    <span class="brand-name">Tembo &amp; Lusani Advocates</span>
  </div>
  <div class="abs brand-tag">CONSTRUCTION LAW &nbsp;|&nbsp; ARBITRATION &nbsp;|&nbsp; LITIGATION</div>
  <div class="abs head-contact" style="left:700px">
    <span class="ico-ring"><svg width="16" height="12" viewBox="0 0 16 12"><rect x="1" y="1" width="14" height="10" fill="none" stroke="#9b1a27" stroke-width="1.6"/><path d="M1 1l7 6 7-6" fill="none" stroke="#9b1a27" stroke-width="1.6"/></svg></span>
    advocates@tembolusani.com
  </div>
  <div class="abs head-contact" style="left:952px">
    <span class="ico-ring"><svg width="14" height="14" viewBox="0 0 24 24"><path d="M6.6 10.8c1.4 2.8 3.8 5.1 6.6 6.6l2.2-2.2c.3-.3.7-.4 1-.2 1.1.4 2.3.6 3.6.6.6 0 1 .4 1 1V20c0 .6-.4 1-1 1C10.6 21 3 13.4 3 4c0-.6.4-1 1-1h3.5c.6 0 1 .4 1 1 0 1.3.2 2.5.6 3.6.1.3 0 .7-.2 1z" fill="#9b1a27"/></svg></span>
    0414 555 210
  </div>

  <nav class="abs nav">
    <ul>
      <li class="active">Home</li><li>Our History</li><li>Who We Are</li><li>How We Do It</li><li>Practice Areas</li><li>Our clients</li><li>Our Professionals</li><li>Contact</li>
    </ul>
  </nav>

  <!-- hero -->
  <div class="abs hero" role="img" aria-label="Lawyer signing a contract at a desk beside a gavel"></div>
  <div class="abs hero-title center">Qualified Legal Advice</div>
  <div class="abs btn" style="left:514px;top:477px;width:158px;height:36px">View More</div>
  <div class="abs arrow" style="left:47px;top:434px"><svg width="12" height="12" viewBox="0 0 12 12"><path d="M8 1L3 6l5 5" fill="none" stroke="#222" stroke-width="2"/></svg></div>
  <div class="abs arrow" style="left:1121px;top:434px"><svg width="12" height="12" viewBox="0 0 12 12"><path d="M4 1l5 5-5 5" fill="none" stroke="#9b1a27" stroke-width="2"/></svg></div>

  <!-- services -->
  <div class="abs sec-title center" style="top:794px">Our Services</div>
  <div class="abs sec-sub center" style="top:846px">Lorem Ipsum is simply dummy text of printing.</div>

  <div class="abs svc-photo" style="left:132px;top:891px;background:linear-gradient(150deg,#cfe3f5 0%,#e9b04a 45%,#3d6fa3 100%)" role="img" aria-label="Engineer with hard hat reviewing plans at a construction site"></div>
  <div class="abs svc-name center" style="left:107px;top:1168px">CONSTRUCTION LAW</div>
  <div class="abs svc-text center" style="left:117px;top:1212px">Lorem Ipsum is simply dummy text of printing and typesetting industry. Lorem Ipsum has been the industry's</div>
  <div class="abs btn" style="left:184px;top:1290px;width:146px;height:34px">View More</div>

  <div class="abs svc-photo" style="left:483px;top:891px;background:linear-gradient(150deg,#d9d4cc 0%,#8c8880 50%,#3a3532 100%)" role="img" aria-label="Scales of justice and documents on a lawyer's desk"></div>
  <div class="abs svc-name center" style="left:458px;top:1168px">COMMERCIAL LITIGATION</div>
  <div class="abs svc-text center" style="left:468px;top:1212px">Lorem Ipsum is simply dummy text of printing and typesetting industry. Lorem Ipsum has been the industry's</div>
  <div class="abs btn" style="left:535px;top:1290px;width:146px;height:34px">View More</div>

  <div class="abs svc-photo" style="left:822px;top:891px;background:linear-gradient(150deg,#5a3a28 0%,#a06a45 45%,#e2cdb5 100%)" role="img" aria-label="Hand holding a magnifying glass over a contract"></div>
  <div class="abs svc-name center" style="left:797px;top:1168px">ARBITRATION</div>
  <div class="abs svc-text center" style="left:807px;top:1212px">Lorem Ipsum is simply dummy text of printing and typesetting industry. Lorem Ipsum has been the industry's</div>
  <div class="abs btn" style="left:874px;top:1290px;width:146px;height:34px">View More</div>

  <!-- professionals -->
  <div class="abs pro" role="img" aria-label="Brass scales of justice and a wooden gavel on law books"></div>
  <div class="abs pro-title center">Our Professionals</div>
  <div class="abs pro-sub center">Lorem Ipsum is dummy text of the printing and typesetting industry.</div>
  <div class="abs btn" style="left:529px;top:1656px;width:146px;height:36px">View More</div>

  <div class="abs stat" style="left:21px;top:1794px">
    <svg width="40" height="34" viewBox="0 0 40 34"><path d="M2 12l8-6 8 4 6-4 14 8-6 8-8 6-8-4-8-4z" fill="none" stroke="#fff" stroke-width="2" stroke-linejoin="round"/><path d="M18 10l-6 6 3 2 6-4" fill="none" stroke="#fff" stroke-width="2"/></svg>
    <div class="stat-label">PARTNERS</div><div class="stat-num">5</div>
  </div>
  <div class="abs stat" style="left:237px;top:1794px">
    <svg width="40" height="34" viewBox="0 0 40 34"><circle cx="20" cy="9" r="5" fill="none" stroke="#fff" stroke-width="2"/><circle cx="8" cy="13" r="4" fill="none" stroke="#fff" stroke-width="2"/><circle cx="32" cy="13" r="4" fill="none" stroke="#fff" stroke-width="2"/><path d="M10 30c0-7 4-11 10-11s10 4 10 11M1 28c0-5 3-8 7-8M39 28c0-5-3-8-7-8" fill="none" stroke="#fff" stroke-width="2"/></svg>
    <div class="stat-label">PEOPLE</div><div class="stat-num">20+</div>
  </div>
  <div class="abs stat" style="left:529px;top:1794px">
    <svg width="40" height="34" viewBox="0 0 40 34"><rect x="4" y="5" width="26" height="24" rx="2" fill="none" stroke="#fff" stroke-width="2"/><path d="M4 12h26M11 2v6M23 2v6" stroke="#fff" stroke-width="2"/><circle cx="30" cy="25" r="7" fill="#1a100b" stroke="#fff" stroke-width="2"/><path d="M30 21v4l3 2" fill="none" stroke="#fff" stroke-width="2"/></svg>
    <div class="stat-label">COMBINED EXPERIENCE</div><div class="stat-num">55</div>
  </div>
  <div class="abs stat" style="left:856px;top:1794px">
    <svg width="40" height="34" viewBox="0 0 40 34"><path d="M10 2h14l7 7v23H10z" fill="none" stroke="#fff" stroke-width="2" stroke-linejoin="round"/><path d="M24 2v7h7" fill="none" stroke="#fff" stroke-width="2"/><path d="M15 20l4 4 7-8" fill="none" stroke="#fff" stroke-width="2"/></svg>
    <div class="stat-label">CASES SOLVED</div><div class="stat-num">350+</div>
  </div>

  <!-- team -->
  <div class="abs sec-title center" style="top:1982px;font-size:30px">Our Team</div>
  <div class="abs sec-sub center" style="top:2021px">Lorem Ipsum is dummy typesetting industry.</div>

  <div class="abs member-photo" style="left:114px;top:2070px" role="img" aria-label="Portrait of Samuel R. Tembo"></div>
  <div class="abs center" style="left:93px;top:2302px;width:260px"><div class="member-name">Samuel. R. Tembo</div><div class="member-role">Managing Partner</div></div>
  <div class="abs socials" style="left:93px;top:2380px;width:260px"><span></span><span></span><span></span></div>

  <div class="abs member-photo" style="left:360px;top:2070px" role="img" aria-label="Portrait of Daniel M. Tembo"></div>
  <div class="abs center" style="left:339px;top:2302px;width:260px"><div class="member-name">Daniel. M. Tembo</div><div class="member-role">Senior Partner</div></div>
  <div class="abs socials" style="left:339px;top:2380px;width:260px"><span></span><span></span><span></span></div>

  <div class="abs member-photo" style="left:611px;top:2070px" role="img" aria-label="Portrait of Grace Lusani"></div>
  <div class="abs center" style="left:590px;top:2302px;width:260px"><div class="member-name">Grace Lusani</div><div class="member-role">Partner</div></div>
  <div class="abs socials" style="left:590px;top:2380px;width:260px"><span></span><span></span><span></span></div>

  <div class="abs member-photo" style="left:861px;top:2070px" role="img" aria-label="Portrait of Peter Okello"></div>
  <div class="abs center" style="left:840px;top:2302px;width:260px"><div class="member-name">Peter Okello</div><div class="member-role">Managing Partner</div></div>
  <div class="abs socials" style="left:840px;top:2380px;width:260px"><span></span><span></span><span></span></div>

  <div class="abs dot" style="left:569px;top:2446px;background:var(--red)"></div>
  <div class="abs dot" style="left:590px;top:2446px"></div>
  <div class="abs dot" style="left:611px;top:2446px"></div>

  <!-- practice tabs -->
  <div class="abs tab center" style="left:84px;top:2518px">Construction<br>&amp; Arbitration</div>
  <div class="abs tab center active" style="left:473px;top:2518px">Commercial Litigation<br>&amp; Transactions</div>
  <div class="abs tab center" style="left:819px;top:2518px">Corporate<br>Advisory</div>
  <div class="abs tab-line"></div>

  <!-- clients -->
  <div class="abs arrow-sm" style="left:62px;top:2683px"><svg width="10" height="10" viewBox="0 0 10 10"><path d="M7 1L3 5l4 4" fill="none" stroke="#fff" stroke-width="2"/></svg></div>
  <div class="abs arrow-sm" style="left:1116px;top:2683px"><svg width="10" height="10" viewBox="0 0 10 10"><path d="M3 1l4 4-4 4" fill="none" stroke="#fff" stroke-width="2"/></svg></div>
  <div class="abs client" style="left:194px;top:2684px">Swiftline</div>
  <div class="abs client" style="left:353px;top:2684px"><i></i>Harvest Co</div>
  <div class="abs client" style="left:512px;top:2684px">Beacon Media</div>
  <div class="abs client" style="left:681px;top:2684px"><i></i>Unity Insure</div>
  <div class="abs client" style="left:842px;top:2684px">Cartwell</div>
  <div class="abs client" style="left:1004px;top:2684px">Motorhaus</div>

  <!-- newsletter -->
  <div class="abs news"></div>
  <div class="abs news-title center">Join The Newletter</div>
  <div class="abs news-sub center">Sign up for Our Newsletter</div>
  <div class="abs news-input">Email here</div>
  <div class="abs news-btn">Subscribe</div>

  <!-- footer -->
  <footer class="abs footer"></footer>
  <div class="abs foot-logo">
    <div class="row"><span class="brand-square"></span><span class="brand-name">Tembo &amp; Lusani Advocates</span></div>
    <small>CONSTRUCTION LAW &nbsp;|&nbsp; ARBITRATION &nbsp;|&nbsp; LITIGATION</small>
  </div>
  <div class="abs foot-text" style="left:118px;top:3200px;width:280px">Lorem Ipsum is simply dummy text the printing and ypesetting industry a been the industry's standard dummy...</div>
  <div class="abs foot-text" style="left:118px;top:3272px">Read More &nbsp;<svg width="12" height="12" viewBox="0 0 12 12"><circle cx="6" cy="6" r="5" fill="none" stroke="#fff" stroke-width="1.4"/><path d="M5 3.5L7.5 6 5 8.5" fill="none" stroke="#fff" stroke-width="1.4"/></svg></div>

  <div class="abs" style="left:426px;top:3106px">
    <div class="foot-head">Head Office Address</div><div class="foot-rule"></div>
    <div class="foot-text" style="margin-top:24px;width:170px">Plot 14, Jacaranda Avenue 2nd Floor, Mvule House<br>P. O Box 4410.<br>Kampala, Uganda</div>
  </div>

  <div class="abs" style="left:615px;top:3106px">
    <div class="foot-head">Contacts</div><div class="foot-rule"></div>
    <div class="foot-text" style="margin-top:24px;line-height:29px">T: 0414 555 210<br>M: +256 (0) 700 555 318<br>E: advocates@tembolusani.com<br>W: www.tembolusani.com</div>
  </div>

  <div class="abs" style="left:845px;top:3106px;width:234px">
    <div class="foot-head">Quick Contact</div><div class="foot-rule"></div>
    <div style="display:flex;gap:6px;margin-top:26px"><div class="field" style="flex:1">Name</div><div class="field" style="flex:1">Phone</div></div>
    <div class="field" style="margin-top:6px;height:54px">Message</div>
    <div class="foot-text" style="text-align:right;font-size:11px;margin-top:8px;padding-right:50px">SEND</div>
  </div>

  <div class="abs copyright">Copyright © 2018 T&amp;L Tembo &amp; Lusani Advocates. All Rights Reserved.</div>
  <div class="abs copy-social"><span></span><span></span><span></span><span></span><span></span></div>

</div>
</body>
</html>
```